" A empresa funciona em um escritório físico, onde os clientes são recebidos para conversar sobre como desejam seu projeto residencial ou comercial. Oferecemos também projetos de decoração, e de instalações, bem como projeto de estrutura. O processo de criação se da tambem pela produção de projetos em 3d. alem da produção do projeto acompanhamos tambem a obra e todo o processo de construção. "

```html
<!DOCTYPE html>
<html lang="pt-BR">
<head>
<meta charset="utf-8">
<title>Lívia Sarandi · Papel timbrado</title>
<link rel="stylesheet" href="https://fonts.googleapis.com/css2?family=Montserrat:wght@300;400&family=Open+Sans:wght@300;400&display=swap">
<style>
  :root {
    --backdrop: #e9e9e7;
    --paper: #ffffff;
    --brand-yellow: #fdd92b;
    --brand-grey: #7b7b7b;
    --text-grey: #8a8a8a;
    --text-light: #a8a8a8;
  }
  * { margin: 0; padding: 0; box-sizing: border-box; }
  html, body { width: 1200px; height: 1200px; overflow: hidden; }
  body {
    background: var(--backdrop);
    font-family: "Open Sans", Arial, sans-serif;
    display: flex;
    align-items: center;
    justify-content: center;
  }
  .letterhead {
    width: 1040px;
    height: 1040px;
    background: var(--paper);
    position: relative;
    padding: 90px 90px;
    box-shadow: 0 2px 10px rgba(0,0,0,0.06);
  }
  .letter-body {
    font-size: 17px;
    line-height: 1.75;
    color: var(--text-grey);
    font-weight: 300;
    max-width: 860px;
  }
  .letter-body p + p { margin-top: 18px; }
  .sender {
    position: absolute;
    left: 90px;
    top: 540px;
    width: 420px;
  }
  .sender-brand {
    display: flex;
    align-items: center;
    gap: 14px;
  }
  .brand-dot {
    width: 34px;
    height: 34px;
    border-radius: 50%;
    background: var(--brand-yellow);
    flex: none;
  }
  .brand-name {
    font-family: "Montserrat", Arial, sans-serif;
    font-weight: 300;
    font-size: 26px;
    letter-spacing: 3px;
    text-transform: uppercase;
    color: var(--brand-grey);
    white-space: nowrap;
  }
  .brand-tagline {
    font-family: "Montserrat", Arial, sans-serif;
    font-weight: 300;
    font-size: 11px;
    letter-spacing: 4px;
    text-transform: uppercase;
    color: var(--text-light);
    margin: 6px 0 0 48px;
  }
  .contact-list {
    list-style: none;
    margin: 34px 0 0 48px;
    font-size: 14px;
    line-height: 1.7;
    color: var(--text-grey);
  }
  .contact-item { display: flex; gap: 12px; align-items: flex-start; }
  .contact-icon { width: 14px; height: 14px; margin-top: 4px; flex: none; fill: var(--text-grey); }
  .brand-feature {
    position: absolute;
    left: 560px;
    top: 500px;
    width: 400px;
    display: flex;
    align-items: center;
    gap: 28px;
  }
  .feature-dot {
    width: 150px;
    height: 150px;
    border-radius: 50%;
    background: var(--brand-yellow);
    flex: none;
  }
  .feature-name {
    font-family: "Montserrat", Arial, sans-serif;
    font-weight: 300;
    font-size: 34px;
    line-height: 1.25;
    letter-spacing: 3px;
    text-transform: uppercase;
    color: var(--brand-grey);
    white-space: nowrap;
  }
</style>
</head>
<body>
  <main class="letterhead">
    <section class="letter-body">
      <p>Lorem ipsum dolor sit amet, consectetur adipiscing elit. Vivamus commodo nisi ut felis dictum, a efficitur arcu suscipit. Sed suscipit eros nec dui fringilla, quis porta ligula tempor. Quisque id sem tincidunt, commodo purus in, bibendum ullamcorper eget condimentum ipsum.</p>
      <p>Aenean amet purus nec blandit sagittis mi. Duis feugiat, dolor nec auctor mollis, est non metus. Proin velit lectus, iaculis at venenatis vitae, auctor quis est. Donec volutpat finibus est. Nam in lacus quis lacus consectetur pretium quis sit amet lacus. Quisque at mauris iaculis, erat felis condimentum dolor, nec maximus velit ipsum eu orci. Quisque at mauris ultrices et est in tempor.</p>
      <p>Proin tincidunt gravida velit id tristique. Proin turpis elit, ultrices et est in tempor mattis purus.</p>
    </section>

    <section class="sender">
      <div class="sender-brand">
        <span class="brand-dot"></span>
        <span class="brand-name">Lívia Sarandi</span>
      </div>
      <div class="brand-tagline">Arquitetura e Urbanismo</div>
      <ul class="contact-list">
        <li class="contact-item">
          <svg class="contact-icon" viewBox="0 0 24 24" aria-hidden="true"><path d="M12 2a7 7 0 0 0-7 7c0 5 7 13 7 13s7-8 7-13a7 7 0 0 0-7-7zm0 9.5A2.5 2.5 0 1 1 12 6.5a2.5 2.5 0 0 1 0 5z"/></svg>
          <span>Rua das Acácias 214, sala 5<br>Centro · Lagoa Serena · Bahia</span>
        </li>
        <li class="contact-item">
          <svg class="contact-icon" viewBox="0 0 24 24" aria-hidden="true"><path d="M6.6 10.8a15.1 15.1 0 0 0 6.6 6.6l2.2-2.2a1 1 0 0 1 1-.25 11.4 11.4 0 0 0 3.6.57 1 1 0 0 1 1 1V20a1 1 0 0 1-1 1A17 17 0 0 1 3 4a1 1 0 0 1 1-1h3.5a1 1 0 0 1 1 1 11.4 11.4 0 0 0 .57 3.6 1 1 0 0 1-.25 1z"/></svg>
          <span>(75) 90000-1234 · 90000-5678</span>
        </li>
      </ul>
    </section>

    <div class="brand-feature">
      <span class="feature-dot"></span>
      <span class="feature-name">Lívia<br>Sarandi</span>
    </div>
  </main>
</body>
</html>
```